We need a card design for our company Pebble Harbor Services. Our goal is to save people money on their disposal services. For this post card please put our logo in it. Please use these colors Pantone 576c and 418c or green and grey. We are giving you as the designer the opportunity to be creative with any other images. We are looking to have a fun eye catching postcard.
Please write:
Think you are stuck with your trash bill? Think again
We cut your neighbors disposal cost by 40%.

Please put down our information also,
Contact us
800.555.0147
marlene@gravelnook.com
gravelnook.com

```html
<!DOCTYPE html>
<html lang="en">
<head>
<meta charset="utf-8">
<title>Pebble Harbor Services – Postcard</title>
<link href="https://fonts.googleapis.com/css2?family=Roboto+Condensed:wght@400;700&display=swap" rel="stylesheet">
<style>
  :root{
    --green:#6f9d2f;
    --green-bright:#7fb236;
    --green-dark:#557f26;
    --green-pale:#e8efd9;
    --grey:#55574f;
    --grey-light:#8a8c84;
    --paper:#ffffff;
    --backdrop:#4a413b;
  }
  *{box-sizing:border-box;margin:0;padding:0}
  html,body{width:1200px;height:500px;overflow:hidden;background:var(--backdrop)}
  body{font-family:"Roboto Condensed",Arial,sans-serif}
  .stage{position:relative;width:1020px;height:425px;transform:scale(1.1765);transform-origin:0 0}

  .card{position:absolute;background:var(--paper);box-shadow:0 4px 14px rgba(0,0,0,.45);overflow:hidden}
  .card--front{left:52px;top:73px;width:432px;height:284px;
    background:linear-gradient(180deg,#fbfcf8 0%,var(--green-pale) 100%)}
  .card--back{left:521px;top:77px;width:451px;height:285px}

  .brand{position:absolute;display:flex;align-items:center;gap:8px;
    font-weight:700;color:var(--green);font-size:21px;white-space:nowrap}
  .brand__dot{width:26px;height:26px;border-radius:50%;background:var(--green)}
  .card--front .brand{left:13px;top:7px;width:265px;height:50px;background:var(--paper);padding-left:10px}
  .card--back .brand{left:22px;top:27px;font-size:22px}

  .goal{position:absolute;left:18px;top:80px;width:212px;height:38px;border-radius:8px;
    background:var(--green);color:#fff;font-size:12.5px;line-height:15px;padding:4px 10px}
  .hook{position:absolute;left:18px;top:132px;width:170px;color:var(--grey);
    font-weight:700;font-size:17px;line-height:21px}
  .email{position:absolute;left:18px;top:190px;font-size:11px;color:var(--grey-light)}
  .email b{font-weight:400;color:var(--green)}
  .mascot{position:absolute;left:176px;top:159px;width:62px;height:63px;border-radius:6px;
    background:radial-gradient(circle at 50% 50%,var(--green-bright),var(--green-dark))}

  .badge{position:absolute;left:236px;top:45px;width:194px;height:194px;border-radius:50%;
    background:var(--green);padding:6px}
  .badge__money{width:100%;height:100%;border-radius:50%;
    background:radial-gradient(circle,#f2f3ef 55%,#b9bcb2 75%,#e7e9e2 100%);
    display:flex;align-items:center;justify-content:center}
  .badge__core{width:140px;height:140px;border-radius:50%;background:var(--green-bright);
    border:3px solid #fff;color:#fff;font-weight:700;font-size:18px;line-height:20px;
    text-align:center;display:flex;align-items:center;justify-content:center;padding:6px}

  .wave{position:absolute;left:0;bottom:0;width:432px;height:90px}
  .contact{position:absolute;left:18px;top:253px;color:#fff;font-size:19px}
  .contact b{font-weight:700}
  .site{position:absolute;left:270px;top:260px;color:#fff;font-weight:700;font-size:13px}

  .stamp{position:absolute;left:322px;top:19px;width:79px;height:87px;border:1.5px solid var(--grey)}
  .photo{position:absolute;left:6px;top:113px;width:213px;height:172px;
    background:linear-gradient(135deg,#ffffff 0%,#8fc14a 55%,#4d6f93 100%)}
  .address-line{position:absolute;left:219px;width:185px;height:1px;background:var(--grey-light)}
</style>
</head>
<body>
<div class="stage">
  <section class="card card--front">
    <div class="brand"><span class="brand__dot"></span>Pebble Harbor Services</div>
    <p class="goal">Our goal is to save people money on their disposal services</p>
    <p class="hook">Think you are stuck with your trash bill?</p>
    <p class="email">Email: <b>marlene@gravelnook.com</b></p>
    <div class="mascot" role="img" aria-label="Cheerful green trash bin mascot giving a thumbs up"></div>
    <div class="badge">
      <div class="badge__money" role="img" aria-label="Ring of stacked banknotes">
        <p class="badge__core">We cut your neighbors disposal cost by 40%.</p>
      </div>
    </div>
    <svg class="wave" viewBox="0 0 432 90" preserveAspectRatio="none" aria-hidden="true">
      <path d="M0,18 Q200,-4 432,10 L432,90 L0,90 Z" fill="var(--green-dark)"/>
      <path d="M0,24 Q210,2 432,14 L432,90 L0,90 Z" fill="var(--green)"/>
      <path d="M140,10 Q300,-4 432,4" stroke="var(--grey)" stroke-width="4" fill="none"/>
    </svg>
    <p class="contact">Contact us: <b>800.555.0147</b></p>
    <p class="site">www: gravelnook.com</p>
  </section>

  <section class="card card--back">
    <div class="brand"><span class="brand__dot"></span>Pebble Harbor Services</div>
    <div class="stamp"></div>
    <div class="photo" role="img" aria-label="Smiling woman holding a green reusable recycling bag"></div>
    <span class="address-line" style="top:166px"></span>
    <span class="address-line" style="top:195px"></span>
    <span class="address-line" style="top:224px"></span>
    <span class="address-line" style="top:252px"></span>
  </section>
</div>
</body>
</html>
```